Kestrel Outsource Group, Inc. Corporate Profile

I need a new corporate profile. I have attached a photoshop sample file and then a PowerPoint of what I need and the order I need it in. I want to create the new profile from the Pattern Grove design using the Kestrel Presentation powerpoint. The pages should be in the Kestrel Presentation Powerpoint. I am available for any questions. This should be 16 total pages and needs a very slick, bold cover page.

Industry/Entity Type

Financial Service

Font styles to use
Serif
Sans Serif

Requirements
Must have
• Bold, professional, colorful

```html
<!DOCTYPE html>
<html lang="en">
<head>
<meta charset="utf-8">
<title>Kestrel Outsource Group Brochure Design</title>
<link rel="stylesheet" href="https://fonts.googleapis.com/css2?family=Arimo:ital,wght@0,400;0,700;1,400&family=Open+Sans:wght@400&family=Tenor+Sans&family=Roboto+Condensed:wght@700&display=swap">
<style>
  :root {
    --stage: #000000;
    --paper: #ffffff;
    --band: #59595b;
    --gold: #d9b24e;
    --gold-deep: #d6a23a;
    --blue: #2f7aa4;
    --ink: #1b1b1b;
    --heading: #6e6e6e;
    --body: #7a7a7a;
    --definition: #c2c2c2;
    --badge-blue: #3b7cc2;
    --badge-navy: #1f5b8f;
    --badge-red: #c4161c;
  }
  * { margin: 0; padding: 0; box-sizing: border-box; }
  html, body { width: 1200px; height: 1000px; overflow: hidden; background: var(--stage); }
  .canvas { position: relative; width: 1200px; height: 1000px; font-family: "Arimo", Arial, sans-serif; }

  .presentation-title {
    position: absolute; left: 40px; top: 38px;
    font-family: "Open Sans", Arial, sans-serif; color: var(--paper);
    font-size: 31px; line-height: 40px; letter-spacing: -0.3px;
  }
  .page-label {
    position: absolute; top: 908px; width: 200px; text-align: center;
    font-family: "Open Sans", Arial, sans-serif; color: var(--paper); font-size: 31px;
  }

  .page { position: absolute; top: 149px; height: 724px; background: var(--paper); overflow: hidden; }
  .page--one { left: 27px; width: 571px; }
  .page--two { left: 609px; width: 559px; }

  .page-heading {
    position: absolute; top: 72px;
    font-family: "Tenor Sans", Georgia, serif; color: var(--heading);
    font-size: 26px; letter-spacing: 0.5px; white-space: nowrap;
  }
  .page--one .page-heading { left: 353px; }
  .page--two .page-heading { left: 56px; }

  .band { position: absolute; left: 0; top: 148px; width: 100%; height: 291px; background: var(--band); }

  .definition {
    position: absolute; left: 0; top: 22px; width: 100%; text-align: center;
    color: var(--definition); font-size: 25px; white-space: nowrap;
  }
  .definition b { font-weight: 700; }
  .definition i { font-style: italic; }
  .banner { position: absolute; left: 0; top: 0; }
  .banner-word {
    position: absolute; font-weight: 700; font-size: 41px; line-height: 38px; letter-spacing: -0.5px;
  }
  .banner-word--mission { left: 28px; top: 98px; color: var(--ink); }
  .banner-word--vision { right: 35px; top: 183px; color: var(--paper); text-align: right; }

  .statement { position: absolute; top: 456px; width: 270px; text-align: center; }
  .statement--mission { left: 20px; }
  .statement--vision { left: 279px; }
  .statement-icon { display: block; margin: 0 auto; }
  .statement-title { margin-top: 6px; font-weight: 700; font-size: 12.5px; }
  .statement--mission .statement-title { color: var(--gold-deep); }
  .statement--vision .statement-title { color: var(--blue); }
  .statement-text { margin: 16px auto 0; width: 236px; color: var(--body); font-size: 11px; line-height: 13.3px; }

  .footer-bar { position: absolute; left: 0; bottom: 0; width: 100%; height: 16px; background: var(--gold); }
  .footer-tab { position: absolute; bottom: 16px; left: 50%; transform: translateX(-50%); }
  .page-number {
    position: absolute; bottom: 16px; left: 0; width: 100%; text-align: center;
    font-size: 7px; color: #555; line-height: 14px;
  }

  .services-list {
    position: absolute; left: 56px; top: 12px; width: 391px; list-style: none;
    color: var(--paper); font-size: 10.6px; line-height: 15.7px; text-align: justify;
  }
  .services-list li { padding-left: 6px; text-indent: -6px; }
  .services-list li::before { content: "\2022\00a0"; }

  .service {
    position: absolute; display: flex; align-items: center; gap: 9px;
    font-family: "Roboto Condensed", Arial, sans-serif; font-weight: 700;
    color: var(--paper); font-size: 15.5px; letter-spacing: 0.2px; white-space: nowrap;
  }

  .affiliations-title {
    position: absolute; top: 482px; left: 0; width: 100%; text-align: center;
    font-size: 15.5px; color: #2a2a2a;
  }
  .badge { position: absolute; }
</style>
</head>
<body>
<div class="canvas">
  <h1 class="presentation-title">Kestrel Outsource Group<br>Brochure Design</h1>

  <section class="page page--one" aria-label="Page 1, Who We Are">
    <h2 class="page-heading">Who We are</h2>
    <div class="band">
      <svg class="banner" width="571" height="291" viewBox="0 0 571 291" aria-hidden="true">
        <defs>
          <linearGradient id="silver" x1="0" y1="0" x2="1" y2="0">
            <stop offset="0" stop-color="#8c8c8c"/>
            <stop offset="0.45" stop-color="#ffffff"/>
            <stop offset="0.8" stop-color="#f2f2f2"/>
            <stop offset="1" stop-color="#b5b5b5"/>
          </linearGradient>
          <linearGradient id="goldFade" x1="0" y1="0" x2="1" y2="0">
            <stop offset="0" stop-color="#d9b24e"/>
            <stop offset="0.85" stop-color="#d9b24e"/>
            <stop offset="1" stop-color="#b89338"/>
          </linearGradient>
        </defs>
        <polygon points="11,72 560,130 11,207" fill="url(#goldFade)"/>
        <polygon points="11,208 571,122 571,152 11,233" fill="url(#silver)"/>
        <polygon points="11,233 571,152 571,291 100,291" fill="var(--blue)"/>
      </svg>
      <p class="definition"><b>kes-trel</b> /’kestrəl/ 1: <i>a quantitative change</i></p>
      <p class="banner-word banner-word--mission">our<br>mission</p>
      <p class="banner-word banner-word--vision">our<br>vision</p>
    </div>

    <article class="statement statement--mission">
      <svg class="statement-icon" width="38" height="38" viewBox="0 0 38 38" aria-hidden="true">
        <circle cx="19" cy="19" r="18" fill="#fff" stroke="#444" stroke-width="1.2"/>
        <polygon points="5,30 17,13 23,21 27,17 34,30" fill="var(--gold)"/>
        <line x1="17" y1="13" x2="17" y2="5" stroke="#444" stroke-width="1.2"/>
        <polygon points="17,5 24,7 17,9" fill="#d9412e"/>
      </svg>
      <h3 class="statement-title">Mission Statement</h3>
      <p class="statement-text">“At Kestrel Outsource Group, Inc. our mission is to provide professional and compliant receivables management solutions built on a foundation of integrity, transparency, and accountability. Our workforce is empowered to deliver superior results, incorporating innovative technology with intelligent analytics.”</p>
    </article>

    <article class="statement statement--vision">
      <svg class="statement-icon" width="38" height="38" viewBox="0 0 38 38" aria-hidden="true">
        <circle cx="19" cy="21" r="16" fill="#222"/>
        <circle cx="19" cy="21" r="12" fill="#fff"/>
        <circle cx="19" cy="21" r="8.5" fill="#222"/>
        <circle cx="19" cy="21" r="5" fill="#fff"/>
        <circle cx="19" cy="21" r="2.5" fill="#d9412e"/>
        <line x1="19" y1="21" x2="29" y2="6" stroke="#555" stroke-width="1.2"/>
        <circle cx="30" cy="5" r="3" fill="#3da2d8"/>
      </svg>
      <h3 class="statement-title">Corporate Vision</h3>
      <p class="statement-text">“Kestrel Outsource Group, remains committed to controlled growth which will be achieved by consistently providing our clients with superior performance and unparalleled customer service as companies seek to align themselves with organizations capable of providing this level of service in a profitable manner while maintaining a vigilant eye oncompliance so as to ensure a mutually beneficial, long standing partnership.”</p>
    </article>

    <svg class="footer-tab" width="52" height="22" viewBox="0 0 52 22" aria-hidden="true"><polygon points="0,22 26,0 52,22" fill="var(--gold)"/></svg>
    <span class="page-number">1</span>
    <div class="footer-bar"></div>
  </section>

  <section class="page page--two" aria-label="Page 2, What We Do">
    <h2 class="page-heading">What We Do</h2>
    <div class="band">
      <ul class="services-list">
        <li>Nationwide provider of collection and receivable management programs.</li>
        <li>Licensed, Insured, Bonded, and Registered to collect nationwide.</li>
        <li>Built an infrastructure to meet the most demanding challenges of the collection industry.</li>
        <li>Kestrel Outsource Group, Inc. employs a highly experienced and motivated workforce that utilizes state of the art technology and strategies.</li>
        <li>As a company with full call center capabilities, Kestrel Outsource Group, Inc. has the expertise and resources to manage the life cycle of an account.</li>
      </ul>

      <div class="service" style="left:68px; top:162px;">
        <svg width="18" height="24" viewBox="0 0 18 24" aria-hidden="true"><rect x="5" y="0" width="8" height="24" rx="2" fill="#b8923a"/><circle cx="9" cy="12" r="7.5" fill="var(--gold)"/><circle cx="9" cy="12" r="5" fill="#fff3cf"/><path d="M9 8v4h3" stroke="#8a6b22" stroke-width="1.4" fill="none"/></svg>
        PRE CHARGE/EARLY OUT
      </div>
      <div class="service" style="left:284px; top:160px;">
        <svg width="20" height="28" viewBox="0 0 20 28" aria-hidden="true"><rect x="1" y="1" width="18" height="26" fill="none" stroke="var(--gold)" stroke-width="2"/><circle cx="11" cy="7" r="2.5" fill="var(--gold)"/><path d="M10 10l-3 6 4 2-2 6M10 11l4 4M8 13l-3 2" stroke="var(--gold)" stroke-width="2" fill="none"/></svg>
        SKIP TRACING
      </div>
      <div class="service" style="left:68px; top:200px;">
        <svg width="20" height="22" viewBox="0 0 20 22" aria-hidden="true"><path d="M10 2v18M4 20h12M3 5h14" stroke="var(--gold)" stroke-width="1.6" fill="none"/><path d="M1 12l2-7 2 7zM15 12l2-7 2 7z" fill="var(--gold)"/></svg>
        PRE &amp; POST LEGAL
      </div>
      <div class="service" style="left:284px; top:200px;">
        <svg width="20" height="22" viewBox="0 0 20 22" aria-hidden="true"><circle cx="10" cy="7" r="5" fill="var(--gold)"/><path d="M4 6a6 6 0 0 1 12 0" stroke="#b8923a" stroke-width="1.6" fill="none"/><path d="M1 22a9 8 0 0 1 18 0z" fill="var(--gold)"/></svg>
        CUSTOMER CARE
      </div>
      <div class="service" style="left:66px; top:237px;">
        <svg width="24" height="24" viewBox="0 0 24 24" aria-hidden="true"><circle cx="12" cy="12" r="11.5" fill="var(--gold)"/><circle cx="12" cy="12" r="8.5" fill="none" stroke="#8a6b22" stroke-width="1"/><text x="12" y="17" text-anchor="middle" font-family="Arimo, Arial, sans-serif" font-weight="700" font-size="13" fill="#5a4414">$</text></svg>
        POST CHARGE OFF
      </div>
    </div>

    <h3 class="affiliations-title">Affiliations</h3>
    <svg class="badge" style="left:29px; top:525px;" width="90" height="88" viewBox="0 0 90 88" role="img" aria-label="Association of credit professionals membership badge">
      <rect x="17" y="2" width="56" height="46" fill="var(--badge-blue)"/>
      <rect x="10" y="56" width="70" height="10" fill="var(--badge-blue)" opacity="0.35"/>
      <rect x="4" y="72" width="82" height="6" fill="#bbbbbb"/>
    </svg>
    <svg class="badge" style="left:169px; top:528px;" width="82" height="82" viewBox="0 0 82 82" role="img" aria-label="State collectors association membership badge">
      <circle cx="41" cy="41" r="40" fill="#1a1a1a"/>
      <circle cx="41" cy="41" r="24" fill="none" stroke="#fff" stroke-width="1.5"/>
    </svg>
    <svg class="badge" style="left:310px; top:524px;" width="54" height="89" viewBox="0 0 54 89" role="img" aria-label="Accredited business badge">
      <rect x="0.5" y="0.5" width="53" height="88" rx="5" fill="#fff" stroke="#9aa7b3"/>
      <rect x="4" y="4" width="46" height="81" rx="3" fill="var(--badge-navy)"/>
    </svg>
    <svg class="badge" style="left:419px; top:544px;" width="108" height="49" viewBox="0 0 108 49" role="img" aria-label="Debt buyers association membership badge">
      <rect x="0" y="0" width="108" height="49" fill="var(--badge-red)"/>
    </svg>

    <svg class="footer-tab" width="52" height="22" viewBox="0 0 52 22" aria-hidden="true"><polygon points="0,22 26,0 52,22" fill="var(--gold)"/></svg>
    <span class="page-number">2</span>
    <div class="footer-bar"></div>
  </section>

  <p class="page-label" style="left:212px;">Page 1</p>
  <p class="page-label" style="left:797px;">Page 2</p>
</div>
</body>
</html>
```